Harold Vane Collective - Juvenile Skeletal Repair Agenda Framing Network

A 2-sided A4 leaflet to explain the research priorities in Children's Orthopaedic Surgery.
We would like this to be similar to that produced previously by the physiotherapists.

```html
<!DOCTYPE html>
<html lang="en">
<head>
<meta charset="utf-8">
<title>Harold Vane Collective – Research Priorities Leaflet</title>
<link href="https://fonts.googleapis.com/css2?family=Lato:wght@400;700;900&display=swap" rel="stylesheet">
<style>
:root{
  --backdrop:#e0e0e0;
  --paper:#fcfbfb;
  --navy:#1e1c5c;
  --ink:#222228;
  --peach:#f5a36a;
  --purple:#3a2ea0;
  --green:#17a878;
  --amber:#f8b31b;
  --red:#e32b39;
  --teal:#0f96a0;
  --teal-ink:#0e8a93;
  --lime:#d8d42a;
  --sage:#9ecbb8;
  --disc:#ebe6e1;
}
*{box-sizing:border-box;margin:0;padding:0}
html,body{width:1200px;height:1200px;overflow:hidden}
body{background:var(--backdrop);font-family:"Lato",sans-serif;color:var(--ink);position:relative}
.page{position:absolute;top:275px;width:464px;height:650px;background:var(--paper);overflow:hidden}
.page--front{left:100px}
.page--back{left:636px}
.abs{position:absolute}

/* partner names */
.partner{position:absolute;display:flex;align-items:center;gap:6px;font-weight:700}
.partner__dot{width:12px;height:12px;border-radius:50%;flex:none}
.partner--albion{color:var(--navy);font-size:10px}
.partner--albion .partner__dot{background:var(--navy)}
.partner--kestrel{background:#fff;color:var(--navy);font-size:12px;padding:0 10px}
.partner--kestrel .partner__dot{background:var(--navy)}
.partner--myls{background:var(--red);color:#fff;font-size:13px;border-radius:9px;padding:0 10px}

/* front */
.title{position:absolute;left:46px;top:112px;font-weight:900;font-size:37px;color:var(--peach);letter-spacing:-.3px;white-space:nowrap}
.subtitle{position:absolute;left:46px;top:160px;font-weight:900;font-size:25px;line-height:28px;color:var(--navy)}
.intro{position:absolute;left:22px;width:420px;font-size:9.8px;line-height:12.8px;text-align:justify}
.band{position:absolute;left:0;top:496px;width:464px;height:154px;background:var(--red)}
.stage{position:absolute;top:339px;width:128px;height:298px;border-radius:22px;background:var(--paper);overflow:hidden;box-shadow:0 0 6px rgba(0,0,0,.15)}
.stage__head{height:82px;color:#fff;text-align:center;font-weight:700;font-size:25px;padding-top:14px}
.stage__num{position:absolute;left:37px;top:53px;width:54px;height:54px;border-radius:50%;color:#fff;font-size:28px;text-align:center;line-height:50px}
.stage__verb{margin-top:38px;text-align:center;font-weight:700;font-size:25px}
.stage__text{padding:6px 12px 0;font-size:8.6px;line-height:11px;text-align:justify}
.stage__text b{font-size:10px;line-height:12px}
.stage--ask .stage__head,.stage--ask .stage__num{background:var(--purple)}
.stage--ask .stage__verb{color:var(--purple)}
.stage--analyse .stage__head,.stage--analyse .stage__num{background:var(--green)}
.stage--analyse .stage__verb{color:var(--green)}
.stage--prioritise .stage__head,.stage--prioritise .stage__num{background:var(--amber)}
.stage--prioritise .stage__verb{color:var(--amber);font-size:19px;padding-top:4px}

/* back */
.heading{position:absolute;left:22px;top:16px;font-size:25px;font-weight:700;color:var(--ink)}
.priority{position:absolute;height:44px;border-radius:14px;display:flex;align-items:center;font-size:8.4px;line-height:10.6px;font-weight:700;box-shadow:0 2px 3px rgba(0,0,0,.2)}
.priority--odd{left:76px;width:364px;padding:0 14px 0 42px;text-align:justify}
.priority--even{left:22px;width:368px;padding:0 42px 0 20px}
.disc{position:absolute;width:52px;height:52px;border-radius:50%;background:var(--disc);box-shadow:1px 2px 4px rgba(0,0,0,.3);text-align:center;line-height:52px;font-size:23px;font-weight:700}
.is-amber{background:var(--amber);color:#fff}
.is-lime{background:var(--lime);color:var(--teal-ink)}
.is-sage{background:var(--sage);color:var(--teal-ink)}
.is-teal{background:var(--teal);color:#fff}
.thanks{position:absolute;left:22px;top:518px;width:424px;font-size:11.5px;line-height:14px;font-weight:700;color:var(--navy)}
.special{position:absolute;left:22px;top:547px;font-size:21px;font-weight:900;color:var(--navy)}
.fairplay{position:absolute;left:22px;top:593px;width:118px;font-size:8.6px;line-height:11px}
</style>
</head>
<body>

<section class="page page--front">
  <div class="partner partner--albion" style="left:42px;top:58px;width:110px;flex-direction:column;text-align:center;gap:4px">
    <span class="partner__dot" style="width:28px;height:28px"></span>Albion Bone Society
  </div>
  <div class="partner partner--kestrel" style="left:156px;top:40px;height:45px">
    <span class="partner__dot"></span>University of Kestrel
  </div>
  <div class="partner partner--myls" style="left:316px;top:48px;height:27px">MYLS</div>

  <h1 class="title">Harold Vane Collective</h1>
  <h2 class="subtitle">Juvenile Skeletal Repair<br>Agenda Framing Network</h2>

  <p class="intro" style="top:223px">Surgery is often carried out amongst children with conditions that their legs, but in many conditions, it is not known which treatment works best. We need high-quality research to test which treatments are better for children.</p>
  <p class="intro" style="top:275px">We reached out to everybody involved with children who have orthopaedic problems affecting their legs (from hip to toes), including children, parents, carers, charity workers, and all the professional groups. We asked all for their views on identifying the most important unanswered questions.</p>

  <div class="band"></div>

  <article class="stage stage--ask" style="left:22px">
    <div class="stage__head">Stage</div>
    <div class="stage__num">1</div>
    <div class="stage__verb">ASK</div>
    <p class="stage__text">Our UK-wide survey of patients, carers, physiotherapists, nurses and surgeons asked <b>“What is the most unanswered question amongst children undergoing planned surgery for conditions affecting</b></p>
  </article>
  <article class="stage stage--analyse" style="left:167px">
    <div class="stage__head">Stage</div>
    <div class="stage__num">2</div>
    <div class="stage__verb">ANALYSE</div>
    <p class="stage__text">We reviewed 1023 questions from 388 people, and sorted these into 76 unique themed questions.</p>
  </article>
  <article class="stage stage--prioritise" style="left:313px">
    <div class="stage__head">Stage</div>
    <div class="stage__num">3</div>
    <div class="stage__verb">PRIORITISE</div>
    <p class="stage__text">From those we asked patients, carers, physiotherapists, nurses and surgeons to tell us <b>“What are your top-10 most important questions”.</b> This created a shortlist that were prioritized at a</p>
  </article>
</section>

<section class="page page--back">
  <h2 class="heading">Our top-10 research priorities:</h2>

  <div class="priority priority--odd is-amber" style="top:50px">What are the best ways to measure the outcome following lower limb orthopaedic surgery in children?</div>
  <div class="disc" style="left:50px;top:46px;color:var(--amber)">01</div>

  <div class="priority priority--even is-lime" style="top:96px">Following orthopaedic surgery to the lower limbs, what should children’s rehabilitation include, how long is it expected to last and how does it affect the result of treatment?</div>
  <div class="disc" style="left:364px;top:92px;color:#b5ac1c">02</div>

  <div class="priority priority--odd is-sage" style="top:143px">What is the short-term and long-term clinical and cost effectiveness of orthopaedic lower limb surgery (including best timing and technique) for children with Cerebral Palsy who can walk?</div>
  <div class="disc" style="left:50px;top:139px;color:var(--teal)">03</div>

  <div class="priority priority--even is-teal" style="top:189px">What are the short term and long term outcomes of surgery compared to non-surgical care in the treatment of Perthes disease of the hip?</div>
  <div class="disc" style="left:364px;top:185px;color:var(--teal)">04</div>

  <div class="priority priority--odd is-lime" style="top:236px">What is the clinical and cost effectiveness of pre-operative rehabilitation in children presenting with lower limb orthopaedic conditions?</div>
  <div class="disc" style="left:50px;top:232px;color:#b5ac1c">05</div>

  <div class="priority priority--even is-amber" style="top:282px">What is the short-term and long-term clinical and cost effectiveness of Selective Dorsal Rhizotomy (SDR) in children with Cerebral Palsy who can walk?</div>
  <div class="disc" style="left:364px;top:278px;color:var(--amber)">06</div>

  <div class="priority priority--odd is-teal" style="top:328px">Can surveillance and non-surgical treatment (e.g. physiotherapy, botulinum toxin injections, functional electrical stimulation, orthotics, casting) prevent the development of deformity requiring surgery in children with Cerebral Palsy?</div>
  <div class="disc" style="left:50px;top:324px;color:var(--teal)">07</div>

  <div class="priority priority--even is-sage" style="top:375px">What is the best method of screening for Developmental Dysplasia of the Hip (DDH) in terms of clinical and cost effectiveness?</div>
  <div class="disc" style="left:364px;top:371px;color:var(--teal)">08</div>

  <div class="priority priority--odd is-lime" style="top:421px">What are the best strategies to optimise communication of information between patients/carers and clinicians in order to enable shared decision-making?</div>
  <div class="disc" style="left:50px;top:417px;color:#b5ac1c">09</div>

  <div class="priority priority--even is-amber" style="top:467px">What is the best management for hip displacement in children with Cerebral Palsy?</div>
  <div class="disc" style="left:364px;top:463px;color:var(--amber)">10</div>

  <p class="thanks">Many thanks to all those people who helped us take this work off the ground and helped us finish it!</p>
  <h3 class="special">Special thanks to:</h3>
  <p class="fairplay">Harold Vane Collective, who always look for fair play in research!</p>

  <div class="partner partner--albion" style="left:130px;top:578px;width:96px;flex-direction:column;text-align:center;gap:3px;font-size:8px">
    <span class="partner__dot" style="width:24px;height:24px"></span>Albion Bone Society
  </div>
  <div class="partner partner--kestrel" style="left:226px;top:583px;height:40px;font-size:10.5px;padding:0 6px">
    <span class="partner__dot" style="width:10px;height:10px"></span>University of Kestrel
  </div>
  <div class="partner partner--myls" style="left:372px;top:590px;height:26px;font-size:12px">MYLS</div>
</section>

</body>
</html>
```